Flyer to promote a conference

Hi, we need an updated flyer style. Looking for a professional conference style based on our website www.brivanteforum.org and the two flyers attached. One is from our first event, second blue one is from our current event we need help with.

We want to feature ~4-8 speakers and 4-8 logos (logos and speaker images can be copied from our one page website).

We are looking for a style to be established and our web design person in house can adjust for fitting our final content in Figma or Illustrator (Figma preferred but not required).

```html
<!DOCTYPE html>
<html lang="en">
<head>
<meta charset="utf-8">
<title>U.S. Brivante Forum 2024 Flyer</title>
<link href="https://fonts.googleapis.com/css2?family=Montserrat:wght@300;400;600;700;800&family=Bebas+Neue&display=swap" rel="stylesheet">
<style>
  :root {
    --orange: #c8622a;
    --orange-dark: #b8561f;
    --paper: #efeeea;
    --white: #ffffff;
    --ink: #333333;
    --muted: #555555;
    --stage: #e4e4e4;
    --frame: #8a8a8a;
  }
  * { box-sizing: border-box; margin: 0; padding: 0; }
  html, body { width: 1200px; height: 1200px; overflow: hidden; }
  body { background: var(--stage); font-family: "Montserrat", Arial, sans-serif; color: var(--ink); position: relative; }

  .flyer { position: absolute; left: 190px; top: 20px; width: 820px; height: 1160px; background: var(--white); overflow: hidden; }

  .masthead { position: absolute; left: 0; top: 0; width: 820px; height: 274px; background: var(--orange); color: var(--white); }
  .masthead__bar { position: absolute; left: 94px; top: 81px; width: 26px; height: 104px; background: var(--white); }
  .masthead__kicker { position: absolute; left: 136px; top: 72px; font-weight: 800; font-size: 45px; letter-spacing: 0.5px; line-height: 1; }
  .masthead__name { position: absolute; left: 132px; top: 111px; font-weight: 800; font-size: 86px; line-height: 1; letter-spacing: 1px; }
  .masthead__year { position: absolute; left: 566px; top: 70px; font-family: "Bebas Neue", Impact, sans-serif; font-size: 156px; line-height: 1; transform: scaleX(0.72); transform-origin: left top; }
  .masthead__meta { position: absolute; left: 0; right: 0; top: 218px; display: flex; justify-content: center; align-items: center; gap: 16px; font-size: 30px; }
  .masthead__date { font-weight: 700; }
  .masthead__sep { font-weight: 300; margin: 0 10px; }
  .masthead__place { font-weight: 300; }

  .intro { position: absolute; left: 0; top: 274px; width: 820px; height: 531px; background: var(--paper); }
  .intro__copy { position: absolute; left: 85px; top: 24px; width: 660px; font-size: 19.5px; line-height: 25px; font-weight: 400; color: #3a3a3a; }
  .intro__copy p + p { margin-top: 16px; }

  .cta { position: absolute; left: 87px; top: 198px; width: 645px; height: 84px; border: 1px solid #777; border-radius: 36px; background: var(--white); overflow: hidden; }
  .cta__label { position: absolute; left: 3px; right: 3px; top: 3px; height: 31px; background: var(--orange); border-radius: 32px 32px 0 0; color: var(--white); font-weight: 800; font-size: 16px; text-align: center; line-height: 31px; }
  .cta__url { position: absolute; left: 0; right: 0; top: 42px; text-align: center; font-size: 27px; font-weight: 400; letter-spacing: 6px; color: #222; }

  .speakers { position: absolute; left: 0; top: 805px; width: 820px; height: 240px; }
  .speakers { top: 578px; height: 467px; background: var(--white); }
  .speakers__title { position: absolute; left: 262px; top: 22px; display: flex; align-items: center; gap: 12px; font-size: 21px; letter-spacing: 4px; font-weight: 400; color: #333; }
  .speakers__title::before { content: ""; width: 14px; height: 14px; background: var(--orange); }

  .speaker-grid { position: absolute; left: 87px; top: 66px; display: grid; grid-template-columns: repeat(4, 150px); column-gap: 20px; row-gap: 62px; }
  .speaker { position: relative; height: 142px; }
  .speaker__frame { position: absolute; left: 0; top: 0; width: 123px; height: 123px; border: 1px solid var(--frame); border-top-left-radius: 20px; }
  .speaker__photo { position: absolute; left: 7px; top: 7px; width: 123px; height: 123px; border-top-left-radius: 20px; border-bottom-right-radius: 20px; }
  .speaker__name { position: absolute; left: 19px; top: 139px; font-size: 12px; color: var(--orange); white-space: nowrap; }
  .speaker__name b { font-weight: 700; text-decoration: underline; text-underline-offset: 2px; }
  .speaker__role { position: absolute; left: 19px; top: 157px; width: 130px; font-size: 8px; line-height: 10px; color: var(--muted); }

  .tone-a { background: linear-gradient(160deg, #e6e6e8, #b9bcc4); }
  .tone-b { background: linear-gradient(160deg, #f1f1f1, #c9b8a6 70%, #2a2a2a); }
  .tone-c { background: linear-gradient(160deg, #d8d8d8, #8c8c8c); }
  .tone-d { background: linear-gradient(160deg, #6b5a4c, #c9a98f 60%, #d3d9e3); }
  .tone-e { background: linear-gradient(160deg, #7a7a7a, #c9a58e 60%, #f2f2f2); }
  .tone-f { background: linear-gradient(160deg, #e8dccd, #c79a73 55%, #9a4f2c); }
  .tone-g { background: linear-gradient(160deg, #f0f0f0, #d2a88b 55%, #1e1e1e); }
  .tone-h { background: linear-gradient(160deg, #4a4a48, #c4a48e 55%, #1f1f1f); }

  .partners { position: absolute; left: 0; top: 1045px; width: 820px; height: 104px; background: var(--paper); display: flex; align-items: center; justify-content: space-between; padding: 0 74px 0 72px; }
  .partner { display: flex; align-items: center; gap: 5px; font-size: 12px; font-weight: 700; color: #333; white-space: nowrap; }
  .partner__dot { width: 11px; height: 11px; border-radius: 50%; background: #333; }
  .partner__sq { width: 11px; height: 11px; background: #333; }
  .flyer__rule { position: absolute; left: 0; bottom: 0; width: 820px; height: 11px; background: var(--orange); }
</style>
</head>
<body>
<main class="flyer">
  <header class="masthead">
    <div class="masthead__bar"></div>
    <div class="masthead__kicker">U.S. BRIVANTE</div>
    <div class="masthead__name">FORUM</div>
    <div class="masthead__year">2024</div>
    <div class="masthead__meta">
      <svg width="40" height="40" viewBox="0 0 40 40" aria-hidden="true">
        <rect x="2" y="6" width="36" height="32" rx="4" fill="none" stroke="#fff" stroke-width="3"/>
        <line x1="2" y1="15" x2="38" y2="15" stroke="#fff" stroke-width="3"/>
        <rect x="10" y="1" width="4" height="9" rx="2" fill="#fff"/>
        <rect x="26" y="1" width="4" height="9" rx="2" fill="#fff"/>
        <g fill="#fff"><rect x="8" y="20" width="6" height="5"/><rect x="17" y="20" width="6" height="5"/><rect x="26" y="20" width="6" height="5"/><rect x="8" y="29" width="6" height="5"/><rect x="17" y="29" width="6" height="5"/><rect x="26" y="29" width="6" height="5"/></g>
      </svg>
      <span class="masthead__date">MAY 28 -29</span>
      <span class="masthead__sep">|</span>
      <span class="masthead__place">Denver, CO</span>
    </div>
  </header>

  <section class="intro">
    <div class="intro__copy">
      <p>In-depth training from the country’s experts in heat pump technology for HVAC and Plumbing professionals.</p>
      <p>Unprecedented growth around heat pump technology offers an exciting new&nbsp; business&nbsp; opportunity for contractors serious about making money, offering quality work, and owning the market.</p>
    </div>
    <div class="cta">
      <div class="cta__label">RESERVE YOUR SEAT TODAY!</div>
      <div class="cta__url">www.brivanteforum.org</div>
    </div>
  </section>

  <section class="speakers">
    <h2 class="speakers__title">FEATURED SPEAKERS</h2>
    <div class="speaker-grid">
      <article class="speaker"><div class="speaker__frame"></div><div class="speaker__photo tone-a" role="img" aria-label="Portrait photo of speaker Martin Lavoie"></div><div class="speaker__name"><b>MARTIN</b> LAVOIE</div><div class="speaker__role">Partner, Build Method Training</div></article>
      <article class="speaker"><div class="speaker__frame"></div><div class="speaker__photo tone-b" role="img" aria-label="Portrait photo of speaker Derek Winslow"></div><div class="speaker__name"><b>DEREK</b> WINSLOW</div><div class="speaker__role">Sr. Technical Manager, Center for Efficient Homes</div></article>
      <article class="speaker"><div class="speaker__frame"></div><div class="speaker__photo tone-c" role="img" aria-label="Black and white portrait photo of speaker Sean Larkin"></div><div class="speaker__name"><b>SEAN</b> LARKIN</div><div class="speaker__role">Vice President, Prairie Appliance and HVAC</div></article>
      <article class="speaker"><div class="speaker__frame"></div><div class="speaker__photo tone-d" role="img" aria-label="Portrait photo of speaker Grant Halvorsen"></div><div class="speaker__name"><b>GRANT</b> HALVORSEN</div><div class="speaker__role">Business Development Manager, Calder Brook</div></article>
      <article class="speaker"><div class="speaker__frame"></div><div class="speaker__photo tone-e" role="img" aria-label="Portrait photo of speaker Keith Carlow"></div><div class="speaker__name"><b>KEITH</b> CARLOW</div><div class="speaker__role">Regional Utilities Sales Manager, Ormond</div></article>
      <article class="speaker"><div class="speaker__frame"></div><div class="speaker__photo tone-f" role="img" aria-label="Portrait photo of speaker Erin Bateman"></div><div class="speaker__name"><b>ERIN</b> BATEMAN</div><div class="speaker__role">Denver Program Manager, Gridwell</div></article>
      <article class="speaker"><div class="speaker__frame"></div><div class="speaker__photo tone-g" role="img" aria-label="Portrait photo of speaker Joel Corrigan"></div><div class="speaker__name"><b>JOEL</b> CORRIGAN</div><div class="speaker__role">Founder, Lumen Tek</div></article>
      <article class="speaker"><div class="speaker__frame"></div><div class="speaker__photo tone-h" role="img" aria-label="Portrait photo of speaker Evan Kessler"></div><div class="speaker__name"><b>EVAN</b> KESSLER</div><div class="speaker__role">TrueLine Tools, Industry Engagement Manager</div></article>
    </div>
  </section>

  <footer class="partners">
    <span class="partner"><span class="partner__dot"></span>Northvale Energy</span>
    <span class="partner">Hartwell Water</span>
    <span class="partner"><span class="partner__sq"></span>FieldCrest</span>
    <span class="partner">Cubix</span>
    <span class="partner"><span class="partner__dot"></span>Ridgeline Power</span>
    <span class="partner">greenhaven homes</span>
  </footer>
  <div class="flyer__rule"></div>
</main>
</body>
</html>
```